Regenerative Medicine Brochure

I want a clean modern bi-fold or tri-fold brochure. We offer non-surgical joint repair for knees, shoulders, and hips. We have many services available including regenerative medicine including stem cell allograft, palatelet rich plasma, prolotherapy, triggerpoint injection, chiropractic and rehab therapies. We are a modern multidisciplinary clinic in coastal California. My logo is already complete and is a vibrant green color. I prefer lots of white space with some areas for service description and what conditions may benefit from the services. Design should convey modern treatments, upscale office and practice, and our target audience is older adults who want to maintain an active pain-free lifestyle.

Target Market(s)

Sports injuries, athletes, seniors who are active, knee pain, shoulder pain, arthritis.

Industry/Entity Type

Alternative Medicine

Font styles to use
Serif

Colors
9bcb3c

Requirements
Must have
• Small white space where we can write date, time, location of next event/class. Colors in brochure to coordinate with logo colors provided.

```html
<!DOCTYPE html>
<html lang="en">
<head>
<meta charset="utf-8">
<title>Harborline Spine &amp; Joint – Regenerative Medicine Brochure</title>
<link rel="stylesheet" href="https://fonts.googleapis.com/css2?family=Open+Sans:ital,wght@0,400;0,600;0,700;1,700&family=Arimo:wght@400;700&display=swap">
<style>
  :root {
    --green: #4cb848;
    --white: #ffffff;
    --ink: #2a2a2a;
    --grey-bg: #5d6164;
    --grey-mid: #c9c9c9;
  }
  * { box-sizing: border-box; margin: 0; padding: 0; }
  html, body { width: 1200px; height: 1200px; overflow: hidden; }
  body {
    background: linear-gradient(180deg, #6a6e71 0%, var(--grey-bg) 100%);
    font-family: "Open Sans", Arial, sans-serif;
    color: var(--ink);
    position: relative;
  }
  .sheet {
    position: absolute;
    left: 30px;
    width: 1140px;
    height: 545px;
    display: flex;
    box-shadow: 0 10px 30px rgba(0,0,0,.35);
  }
  .sheet--outside { top: 30px; }
  .sheet--inside { top: 625px; }
  .panel {
    position: relative;
    width: 380px;
    height: 100%;
    overflow: hidden;
    background: var(--white);
  }
  .panel + .panel { border-left: 1px solid rgba(0,0,0,.06); }
  .band-bottom {
    position: absolute; left: 0; right: 0; bottom: 0;
    height: 58px; background: var(--green);
  }

  /* Back panel */
  .details { padding: 30px 30px 0; font-size: 10.6px; line-height: 1.5; }
  .details h2 {
    color: var(--green); font-style: italic; font-weight: 700;
    font-size: 12.5px; line-height: 1.3; margin-bottom: 6px;
  }
  .details p { margin-bottom: 10px; text-align: justify; }

  /* Event panel */
  .event-panel { background: linear-gradient(180deg, #f4f4f4 0%, var(--grey-mid) 100%); }
  .event-curve { position: absolute; top: 0; left: 0; width: 380px; height: 230px; }
  .event-lines { position: absolute; left: 60px; right: 40px; top: 300px; }
  .event-lines span {
    display: block; height: 24px;
    border-bottom: 2px dotted #555;
  }

  /* Cover */
  .cover-brand { padding: 44px 34px 0; }
  .brand-name {
    display: flex; align-items: flex-start; gap: 12px;
    font-size: 26px; font-weight: 600; color: var(--ink); line-height: 1.15;
  }
  .brand-name .square { flex: none; width: 24px; height: 24px; margin-top: 4px; background: var(--green); }
  .brand-tag { color: var(--green); font-size: 14.5px; margin-top: 22px; line-height: 1.4; }
  .cover-photo {
    position: absolute; left: 0; right: 0; top: 230px; bottom: 58px;
    background:
      radial-gradient(circle at 45% 45%, rgba(214,80,90,.85) 0%, rgba(214,80,90,.35) 22%, transparent 42%),
      linear-gradient(160deg, #f4f6fa 0%, #a9bde0 45%, #5d7fc0 100%);
  }
  .cover-phone {
    position: absolute; left: 28px; bottom: 74px;
    display: flex; align-items: center; gap: 10px;
    color: var(--white); font-weight: 700; font-size: 32px; letter-spacing: 1px;
  }
  .cover-contact {
    position: absolute; left: 28px; right: 10px; bottom: 8px;
    color: var(--white); font-size: 14px; line-height: 1.45;
  }

  /* Services panel */
  .services h2 {
    background: var(--green); color: var(--white);
    font-family: "Arimo", Arial, sans-serif; font-size: 22px; font-weight: 700;
    padding: 8px 0 6px 68px; height: 42px;
  }
  .service-grid {
    display: grid; grid-template-columns: 1fr 1fr;
    grid-auto-rows: 1fr; height: calc(100% - 42px);
  }
  .service { position: relative; display: flex; flex-direction: column; }
  .service .photo { flex: 1; }
  .service .label {
    background: var(--green); color: var(--white);
    font-family: "Arimo", Arial, sans-serif; font-weight: 700; font-size: 12.5px;
    padding: 3px 10px; text-align: center;
  }
  .tone-cells { background: linear-gradient(135deg, #1d4f8c, #5fa3d8 60%, #b35050); }
  .tone-car { background: linear-gradient(135deg, #9bb4c6, #d8cfc4 60%, #3d5a8a); }
  .tone-chiro { background: linear-gradient(135deg, #7b7a78, #d9c2ae 60%, #eee); }
  .tone-back { background: linear-gradient(135deg, #e3e3e3, #a8a8a8 60%, #5d5f66); }
  .tone-neck { background: linear-gradient(135deg, #c9d3c0, #8a2a3c 60%, #3a2a24); }
  .tone-hand { background: linear-gradient(135deg, #e8e4de, #7d6654 60%, #3b3b3b); }
  .tone-rehab { background: linear-gradient(135deg, #eef3f7, #b8c9db 55%, #5b84b1); }
  .tone-knee { background: linear-gradient(135deg, #6b7a6a, #a57a5c 55%, #2b2b2b); }

  /* Q&A panel */
  .qa { padding: 30px 30px 0; font-family: "Arimo", Arial, sans-serif; font-size: 10.8px; line-height: 1.45; }
  .qa p { margin-bottom: 10px; text-align: justify; }
  .qa h3 { color: var(--green); font-weight: 400; font-size: 12.5px; margin: 12px 0 2px; }
  .qa .q { margin-bottom: 0; }
  .areas {
    display: grid; grid-template-columns: repeat(3, 1fr);
    list-style: none; margin: 4px 0 12px;
  }
  .areas li::before { content: "• "; }

  /* Green info panel */
  .info { background: var(--green); color: var(--white); padding: 30px 30px 0;
    font-family: "Arimo", Arial, sans-serif; font-size: 10.8px; line-height: 1.45; }
  .info p { margin-bottom: 12px; text-align: justify; }
  .info h3 { font-weight: 400; font-size: 12.5px; margin-top: 4px; }
</style>
</head>
<body>

<section class="sheet sheet--outside" aria-label="Brochure outside">
  <article class="panel back-panel">
    <div class="details">
      <h2>What can I expect from regenerative medicine treatments?</h2>
      <p>During your visit, the team begins with a consultation and physical exam to determine if you're a candidate for regenerative medicine. They ask about your symptoms, condition, overall health, and lifestyle. If you're a candidate, the team then explains the procedure and what to expect both during and afterward.</p>
      <p>For the procedure, the team first cleans your skin and applies a topical numbing cream to your skin, if needed. Next, the team injects regenerative products into the treatment area. You may feel a slight pinch or burning sensation during the injection. The injection takes less than five minutes and you can return to your usual activities the same day. Mild soreness at the injection site is possible for two to three days.</p>
      <p>Over the coming weeks and months, the injected products help repair damaged tissues at the treatment site. Most people notice results after two months. Follow-up care may be recommended based on your condition and initial results. The team has seen dramatic results with regenerative medicine treatments, however, individual results can vary.</p>
      <p>Speak to the team to see if regenerative medicine is right for you.</p>
      <p>To learn more, schedule a visit online or by phone at Harborline Spine &amp; Joint now.</p>
    </div>
    <div class="band-bottom"></div>
  </article>

  <article class="panel event-panel">
    <svg class="event-curve" viewBox="0 0 380 230" aria-hidden="true">
      <path d="M0 0 H380 V150 Q200 250 0 190 Z" fill="var(--green)"/>
    </svg>
    <div class="event-lines" aria-label="Space for next event date, time and location">
      <span></span><span></span><span></span><span></span><span></span><span></span><span></span>
    </div>
    <div class="band-bottom"></div>
  </article>

  <article class="panel cover">
    <div class="cover-brand">
      <div class="brand-name"><span class="square" aria-hidden="true"></span><span>Harborline Spine &amp; Joint</span></div>
      <div class="brand-tag">Regenerative Medicine Specialists<br>Seaside Bay CA</div>
    </div>
    <div class="cover-photo" role="img" aria-label="Photo of a hand holding a painful knee, highlighted in red on a blue-toned body"></div>
    <div class="cover-phone">
      <svg width="18" height="26" viewBox="0 0 18 26" aria-hidden="true">
        <path d="M6 1 L10 7 L7 10 Q8 16 12 19 L15 16 L18 21 L14 25 Q2 20 1 5 Z" fill="#fff"/>
      </svg>
      805.555.0142
    </div>
    <div class="band-bottom"></div>
    <div class="cover-contact">2150 Coastline Ave Seaside Bay, CA 93000<br>www.harborlinespinejoint.com</div>
  </article>
</section>

<section class="sheet sheet--inside" aria-label="Brochure inside">
  <article class="panel services">
    <h2>SERVICES</h2>
    <div class="service-grid">
      <div class="service"><div class="photo tone-cells" role="img" aria-label="Microscopic cell illustration"></div><div class="label">Regenerative-Medicine</div></div>
      <div class="service"><div class="photo tone-car" role="img" aria-label="Man holding his neck beside a car"></div><div class="label">Auto-Injury-Treatment</div></div>
      <div class="service"><div class="photo tone-chiro" role="img" aria-label="Chiropractor adjusting a patient's shoulder"></div><div class="label">Chiropractic-care</div></div>
      <div class="service"><div class="photo tone-back" role="img" aria-label="Man seated on a sofa holding his lower back"></div><div class="label">Sciatica</div></div>
      <div class="service"><div class="photo tone-neck" role="img" aria-label="Woman holding her neck in discomfort"></div><div class="label">Fibromyalgia</div></div>
      <div class="service"><div class="photo tone-hand" role="img" aria-label="Hands with joint pain"></div><div class="label">Arthritis</div></div>
      <div class="service"><div class="photo tone-rehab" role="img" aria-label="Therapist examining a patient's shoulder"></div><div class="label">Rehabilitation</div></div>
      <div class="service"><div class="photo tone-knee" role="img" aria-label="Runner holding a sore knee"></div><div class="label">Knee-Pain</div></div>
    </div>
  </article>

  <article class="panel qa">
    <p>For joint arthritis and muscle pain and injuries, the team at Harborline Spine &amp; Joint offers minimally invasive regenerative medicine techniques to help you recover from chronic pain. Located in Seaside Bay, California, the medical team utilizes advanced restorative techniques to support the natural healing of injured joints and soft tissues without the need for surgery. To learn more, schedule a consultation online or by phone today.</p>
    <h3>Regenerative Medicine Q &amp; A</h3>
    <p class="q">What is regenerative medicine?</p>
    <p>Regenerative medicine is a form of biotechnology that involves injecting regenerative medicine products into injured tissues to help your body repair damage. Regenerative medicine uses tissue engineering techniques to repair muscles. The medical providers at Harborline Spine &amp; Joint select from a variety of available treatments and products. These include amniotic allografts, hyaluronic acid, regenerative cells, and cytokines which are powerful growth factors that may help regenerate your own body's tissues.</p>
    <p>After you're injection with the amniotic allograft serum, the growth factors trigger repair at the site of injection. Over the course of the next several weeks, cells grow and multiply forming new tissue.</p>
    <h3>Regenerative medicine may be used in the following areas:</h3>
    <ul class="areas">
      <li>Shoulder</li><li>Wrist</li><li>Hip</li>
      <li>Elbow</li><li>Knee</li><li>Ankle</li>
    </ul>
    <p>There are many additional types of bone and soft tissue problems, including arthritis, that these injections may benefit.</p>
  </article>

  <article class="panel info">
    <p>With regenerative medicine and amniotic allograft treatments, the team supports the natural healing abilities of your body without the need for drugs or surgical repair and painful recovery. However, not all forms of regenerative medicine are equal. At Harborline Spine &amp; Joint, the team only works with the best regenerative medicine labs to ensure that the right kind of products are selected and that they are of the best quality and highest safety.</p>
    <h3>How does regenerative medicine work?</h3>
    <p>The team uses lab-grade products that are sterilized and processed to inject into the injured area. Once injected, it is thought that these powerful products differentiate into a variety of tissues to trigger your own body to repair damaged tissues. This damage may involve minor tears in muscles, ligaments, and tendons, or cartilage and meniscus breakdown in joints.</p>
    <p>Regenerative medicine products contain the basic building blocks of the body tissues — including proteins, amino acids, and cytokines — responsible for healing and tissue growth. They also provide anti-inflammatory benefits by promoting repair of tissues affected by inflammation.</p>
    <p>While some inflammation is normal and has a benefit to healing injuries, long-term inflammation causes pain, swelling, and further damage to tissues. When you experience too much inflammation, it does more harm than good. Instead of constantly relying on anti-inflammatory medications, regenerative products may be able to correct the problem at the source and reduce the production of natural inflammatory chemicals so you can heal.</p>
  </article>
</section>

</body>
</html>
```